Need new to-go sticker labels for my restaurant

I need to go sticker labels that are Modern, eye catching and sleek for sushi restaurant. Or it can be really nostalgic. Please include our logo somehow. It will be printed on a 1" x 2.65" label.

I need to also change each label name and price. Or can you tell me how to change each one or do I send you each label name and price?

Example:

California Roll.
Crab, Avocado, Cucumber
$8.99

Target Market(s)

Health conscious.

Industry/Entity Type

Restaurant

Requirements
Must have
• fresh food appeal. Nostalgia and warmth. Don't make it cookie cutter and just stick buxa logo and sushi name, create a picture!! Create something very creative and infuse picture with logo.
Nice to have
• Warmth, nostalgia, fresh looking. Prefer warm tones with fresh appeal. Pick and choose Lime green, red, yellow are fine. Other colors can be used to make exciting!! must catch eye!!! Customers buy WITH THEIR EYES!!!
Should not have
• Should Not be cookie cutter and unnoticed.

```html
<!DOCTYPE html>
<html lang="en">
<head>
<meta charset="utf-8">
<title>Buxa To-Go Label – California Roll</title>
<link href="https://fonts.googleapis.com/css2?family=Arimo:wght@700&family=Archivo+Narrow:wght@700&display=swap" rel="stylesheet">
<style>
  :root {
    --canvas: #ffffff;
    --label-red: #ff0a00;
    --band-black: #0a0a0a;
    --panel-cream: #fdfbd3;
    --text-black: #111111;
    --title-red: #f20f00;
    --divider-tan: #c9a25a;
    --coin-gold: #c9a063;
    --coin-edge: #a9803f;
    --price-yellow-top: #fefbd0;
    --price-yellow-bottom: #fff700;
  }
  * { margin: 0; padding: 0; box-sizing: border-box; }
  html, body {
    width: 1200px; height: 1000px; overflow: hidden;
    background: var(--canvas);
  }
  .label {
    position: absolute; left: 203px; top: 351px;
    width: 795px; height: 298px;
    background: var(--label-red);
    overflow: hidden;
  }
  .brand-band {
    position: absolute; left: 19px; top: 0;
    width: 169px; height: 298px;
    background: var(--band-black);
  }
  .brand-panel {
    position: absolute; left: 19px; top: 46px;
    width: 169px; height: 206px;
    background: #fff;
    display: flex; align-items: flex-end; justify-content: center;
    padding-bottom: 20px;
  }
  .brand-name {
    font-family: "Arimo", Arial, sans-serif;
    font-weight: 700; font-size: 44px; letter-spacing: 6px;
    color: var(--title-red);
  }
  .brand-mark {
    position: absolute; left: 54px; top: 40px;
    width: 60px; height: 60px; background: var(--title-red);
  }
  .menu-frame {
    position: absolute; left: 188px; top: 27px;
    width: 582px; height: 243px;
    background: var(--band-black);
    border-radius: 0 80px 80px 0;
  }
  .menu-panel {
    position: absolute; left: 188px; top: 44px;
    width: 565px; height: 209px;
    background: var(--panel-cream);
    border-radius: 0 62px 62px 0;
  }
  .price-box {
    position: absolute; left: 355px; top: 179px;
    width: 209px; height: 119px;
    background: linear-gradient(180deg, var(--price-yellow-top) 0%, var(--price-yellow-bottom) 100%);
  }
  .item-title {
    position: absolute; left: 188px; top: 62px; width: 565px;
    text-align: center;
    font-family: "Arimo", Arial, sans-serif;
    font-weight: 700; font-size: 55px; line-height: 1;
    color: var(--title-red);
  }
  .item-ingredients {
    position: absolute; left: 188px; top: 126px; width: 565px;
    display: flex; justify-content: center; align-items: center; gap: 8px;
    font-family: "Archivo Narrow", "Arial Narrow", sans-serif;
    font-weight: 700; font-size: 43px; line-height: 1;
    color: var(--text-black);
  }
  .divider {
    display: inline-block; width: 2px; height: 34px;
    background: var(--divider-tan);
  }
  .price-coin {
    position: absolute; left: 300px; top: 196px;
    width: 86px; height: 86px;
  }
  .item-price {
    position: absolute; left: 400px; top: 217px;
    font-family: "Arimo", Arial, sans-serif;
    font-weight: 700; font-size: 60px; line-height: 1;
    color: var(--text-black);
  }
</style>
</head>
<body>
  <div class="label">
    <div class="brand-band"></div>
    <div class="brand-panel">
      <span class="brand-mark"></span>
      <span class="brand-name">BUXA</span>
    </div>
    <div class="menu-frame"></div>
    <div class="menu-panel"></div>
    <div class="price-box"></div>

    <h1 class="item-title">California Roll</h1>
    <p class="item-ingredients">
      <span>Crab</span><span class="divider"></span><span>Avocado</span><span class="divider"></span><span>Cucumber</span>
    </p>

    <svg class="price-coin" viewBox="0 0 86 86" aria-hidden="true">
      <circle cx="43" cy="43" r="42" fill="var(--coin-edge)"/>
      <circle cx="43" cy="43" r="37" fill="var(--coin-gold)"/>
      <text x="43" y="60" text-anchor="middle" font-family="Arimo, Arial, sans-serif" font-weight="700" font-size="50" fill="#ffffff">$</text>
    </svg>
    <p class="item-price">8.99</p>
  </div>
</body>
</html>
```